Chart your Success

We need a website designed for a life coaching company who specialises in one on one coaching, workshops and seminars where they teach participants in goal setting and how to achieve them for a better life.

Objectives

·         Easy to use

·         Clear & concise

·         Quality but not too flashy

·         Shows clearly what you do and how you interact with clients

·         No fuss, straight up

·         Gives those who hear your name or business name a place to go to obtain further information on what I am doing, why & how they can use my services.

·         A way for clients to contact you

·         Seminar & workshop bookings (not mandatory)

·         Most of the website to be static.

Number of Pages Required

1 page

Requirements
Must have
• Sitemap

• Home
• About Us
• One on One Coaching
• Workshops/Seminars
• How we Work?
• Pricing
• Testimonials
• Contact Us

• Design/Content Brief

• ü  The following elements are included in the design/content brief which this proposal is based on:

• o    Flash banner with some images rotating that reflect your business.

• o    Logo and phone number 0438 760 214 will be prominently displayed.

• o    Horizontal Navigation

• o    Contact Us icon on homepage

• o    Sign up for our newsletter on homepage

• o    Privacy Policy/Sitemap/Terms & Conditions in footer

• o    - larger rounded buttons

• o    - good size font

• o    - not having to scroll too far

• o    - soft feel, but not fluffy (images will enhance this)

• ü  Colours that could be used with logo

• o   What about this?  RGB 128,128,128

• o   What about this?  RGB 54, 95, 145

• o   What about this?  RGB 51, 204, 51

• o   Red – R255

• ü   http://www.plumvexlo.com/

• o    I like this website and its rounded buttons, large easy to see and use.

• o    Soft colours

• o    Changing pictures at the top of screen

• Files

```html
<!DOCTYPE html>
<html lang="en">
<head>
<meta charset="utf-8">
<title>Brightmoor Pathways</title>
<link rel="stylesheet" href="https://fonts.googleapis.com/css2?family=Ubuntu:wght@500;700&family=Noto+Serif:wght@700&family=Arimo:wght@400;700&display=swap">
<style>
  :root {
    --red: #e50914;
    --red-dark: #a8000a;
    --grey-frame: #9a9a9a;
    --text: #3d3d3d;
    --ink: #111;
    --lime-top: #eef78a;
    --lime-bottom: #b6d21a;
    --lime-edge: #9dbb10;
    --orange-top: #fbd77d;
    --orange-bottom: #f3a624;
    --orange-edge: #e59a17;
    --cyan-top: #a9e6f3;
    --cyan-bottom: #3fbfdc;
    --cyan-edge: #1fa7c9;
    --sky-top: #2f7fd0;
    --sky-bottom: #bfe1f7;
    --grass: #5fae2b;
  }
  * { box-sizing: border-box; margin: 0; padding: 0; }
  html, body { width: 1200px; height: 900px; overflow: hidden; background: #fff; }
  body { font-family: "Arimo", Arial, sans-serif; color: var(--text); }
  .page { position: relative; width: 1200px; height: 900px; }

  .page-frame {
    position: absolute; left: 61px; top: 94px; width: 1073px; height: 759px;
    border: 3px solid var(--grey-frame); border-radius: 70px;
    box-shadow: 0 0 14px rgba(0,0,0,.18);
    background: #fff;
  }
  .banner {
    position: absolute; left: 293px; top: 94px; width: 841px; height: 200px;
    border-radius: 0 70px 0 0;
    background: linear-gradient(180deg, var(--sky-top) 0%, #6fb0e6 45%, var(--sky-bottom) 78%, var(--grass) 90%, #3f8c1c 100%);
  }
  .banner-team {
    position: absolute; left: 375px; top: 33px; width: 415px; height: 260px;
    border-radius: 90px 90px 0 0;
    background: linear-gradient(180deg, #e9e6e1 0%, #cfc8bd 60%, #b9b2a7 100%);
  }
  .banner-clipboard {
    position: absolute; left: 830px; top: 48px; width: 190px; height: 350px;
    transform: rotate(9deg);
    border-radius: 10px;
    background: linear-gradient(180deg, #3b3b3b 0%, #1d1d1d 100%);
    box-shadow: 4px 6px 12px rgba(0,0,0,.35);
  }
  .banner-clipboard::after {
    content: ""; position: absolute; left: 12px; top: 26px; right: 12px; bottom: 14px;
    background: linear-gradient(180deg, #fff, #eee);
  }

  .contact-bar {
    position: absolute; right: 100px; top: 16px;
    display: flex; align-items: center; gap: 12px;
    font-family: "Ubuntu", sans-serif; font-weight: 700; font-size: 17px; color: var(--ink);
  }
  .contact-icon { width: 30px; height: 18px; }

  .logo {
    position: absolute; left: 59px; top: 53px; width: 292px; height: 292px;
    border-radius: 50%; background: #fff;
    box-shadow: 0 0 16px rgba(0,0,0,.28);
    display: flex; align-items: center; justify-content: center; text-align: center;
  }
  .logo-name {
    font-family: "Noto Serif", Georgia, serif; font-weight: 700;
    font-size: 38px; line-height: 1.15; color: var(--red);
  }

  .main-nav { position: absolute; left: 352px; top: 260px; display: flex; gap: 13px; }
  .nav-bubble {
    position: relative; width: 182px; height: 90px;
    border-radius: 50%;
    background: radial-gradient(ellipse at 50% 30%, var(--lime-top) 0%, #d6ea48 50%, var(--lime-bottom) 100%);
    border: 2px solid var(--lime-edge);
    box-shadow: 0 3px 6px rgba(0,0,0,.2);
    display: flex; align-items: center; justify-content: center; text-align: center;
    font-family: "Ubuntu", sans-serif; font-weight: 700; font-size: 18px; line-height: 1.4;
    color: var(--ink); text-decoration: none;
    text-shadow: 0 1px 0 rgba(255,255,255,.6);
  }
  .nav-bubble::after {
    content: ""; position: absolute; right: 22px; bottom: -14px;
    border-left: 22px solid transparent; border-top: 20px solid var(--lime-bottom);
    transform: skewX(-20deg);
  }

  .page-title {
    position: absolute; left: 102px; top: 377px;
    font-family: "Noto Serif", Georgia, serif; font-weight: 700;
    font-size: 36px; letter-spacing: 4px; color: var(--red); white-space: nowrap;
  }
  .title-rule {
    position: absolute; left: 102px; top: 441px; width: 477px; height: 9px;
    background: linear-gradient(180deg, #ff3b3b, var(--red-dark));
  }
  .feature-list { position: absolute; left: 102px; top: 461px; list-style: none; }
  .feature-list li {
    position: relative; padding-left: 20px;
    font-size: 15.5px; line-height: 21.7px; color: var(--text); white-space: nowrap;
  }
  .feature-list svg { position: absolute; left: 0; top: 5px; width: 15px; height: 13px; }

  .video-player { position: absolute; left: 158px; top: 579px; width: 311px; height: 258px; background: #000; }
  .video-frame {
    position: absolute; left: 0; top: 27px; width: 311px; height: 177px;
    background: linear-gradient(160deg, #c9d9a6 0%, #7ea355 45%, #5d8f2f 100%);
  }
  .video-play { position: absolute; left: 123px; top: 89px; width: 66px; height: 50px; }
  .video-brand {
    position: absolute; right: 8px; top: 210px;
    font-weight: 700; font-size: 14px; color: #fff;
  }
  .video-controls {
    position: absolute; left: 0; bottom: 0; width: 311px; height: 28px;
    background: linear-gradient(180deg, #f2f2f2, #cfcfcf);
    border: 1px solid #aaa;
    display: flex; align-items: center; gap: 8px; padding: 0 6px;
    font-size: 12px; color: #222;
  }
  .video-progress { width: 105px; height: 6px; border-radius: 3px; background: #999; position: relative; }
  .video-progress::before {
    content: ""; position: absolute; left: -3px; top: -4px; width: 14px; height: 14px;
    border-radius: 50%; background: #eee; border: 1px solid #666;
  }

  .feature-tile {
    position: absolute; top: 436px; width: 195px; height: 183px;
    border-radius: 24px; border: 2px solid var(--orange-edge);
    background: linear-gradient(180deg, var(--orange-top) 0%, #f8c25a 55%, var(--orange-bottom) 100%);
    box-shadow: 0 2px 6px rgba(0,0,0,.2);
    text-decoration: none;
  }
  .tile-how { left: 659px; }
  .tile-testimonials { left: 864px; }
  .tile-photo {
    position: absolute; left: 16px; right: 16px; top: 30px; height: 100px;
    border-radius: 40px 40px 0 0;
    background: linear-gradient(180deg, #e8d9c0 0%, #b59677 100%);
  }
  .tile-label {
    position: absolute; left: 10px; right: 10px; top: 133px;
    border-top: 3px solid var(--ink); padding-top: 2px; text-align: center;
    font-family: "Ubuntu", sans-serif; font-weight: 700; font-size: 22px; color: var(--ink);
    white-space: nowrap;
  }

  .newsletter {
    position: absolute; left: 656px; top: 631px; width: 405px; height: 187px;
    border-radius: 26px; border: 2px solid var(--cyan-edge);
    background: linear-gradient(180deg, var(--cyan-top) 0%, #6fd2ea 40%, var(--cyan-bottom) 100%);
    box-shadow: 0 2px 6px rgba(0,0,0,.2);
  }
  .newsletter-title {
    position: absolute; left: 24px; top: 16px; width: 355px;
    border-bottom: 3px solid var(--ink); padding-bottom: 3px;
    font-family: "Ubuntu", sans-serif; font-weight: 700; font-size: 27px; color: var(--ink);
  }
  .newsletter-text {
    position: absolute; left: 26px; top: 63px; width: 360px;
    font-family: "Ubuntu", sans-serif; font-weight: 500; font-size: 15px; line-height: 22px; color: var(--ink);
  }
  .newsletter-input {
    position: absolute; left: 29px; top: 133px; width: 261px; height: 22px;
    border: 1px solid #6a6a6a; background: #fff;
  }
  .newsletter-submit {
    position: absolute; left: 311px; top: 133px; width: 66px; height: 22px;
    border-radius: 11px; border: 1px solid #888;
    background: linear-gradient(180deg, #fff, #cfcfcf);
    font-family: "Arimo", Arial, sans-serif; font-weight: 700; font-size: 14px; color: #222;
  }

  .site-footer {
    position: absolute; left: 0; top: 865px; width: 1200px; text-align: center;
    font-size: 13px; color: #111;
  }
  .site-footer .copyright { margin-right: 22px; }
  .site-footer .sep { margin: 0 8px; }
</style>
</head>
<body>
<div class="page">
  <div class="page-frame"></div>

  <div class="banner" role="img" aria-label="Rotating banner photo of blue sky over green grass"></div>
  <div class="banner-team" role="img" aria-label="Photo of a smiling group of coaching clients standing together"></div>
  <div class="banner-clipboard" role="img" aria-label="Photo of a clipboard with a decisions mind map: who, what, when, where, why, how"></div>

  <div class="contact-bar">
    <span class="phone">0438 760 214</span>
    <svg class="contact-icon" viewBox="0 0 30 18" aria-label="Contact us">
      <rect x="0.5" y="0.5" width="29" height="17" fill="#111"/>
      <polyline points="1,1 15,11 29,1" fill="none" stroke="#fff" stroke-width="1.5"/>
      <line x1="1" y1="17" x2="11" y2="8" stroke="#fff" stroke-width="1.2"/>
      <line x1="29" y1="17" x2="19" y2="8" stroke="#fff" stroke-width="1.2"/>
    </svg>
  </div>

  <div class="logo"><span class="logo-name">Brightmoor<br>Pathways</span></div>

  <nav class="main-nav">
    <a class="nav-bubble" href="#about">about us</a>
    <a class="nav-bubble" href="#coaching">1 on 1<br>coaching</a>
    <a class="nav-bubble" href="#workshops">workshops<br>&amp; seminars</a>
    <a class="nav-bubble" href="#pricing">pricing</a>
  </nav>

  <h1 class="page-title">Chart your Success</h1>
  <div class="title-rule"></div>
  <ul class="feature-list">
    <li><svg viewBox="0 0 15 13"><path d="M1 7 L5 11 L14 1" fill="none" stroke="#e50914" stroke-width="3"/></svg>Donec posuere lobortis nisl, et semper mauris egestas quis.</li>
    <li><svg viewBox="0 0 15 13"><path d="M1 7 L5 11 L14 1" fill="none" stroke="#e50914" stroke-width="3"/></svg>In at enim non lacus volutpat auctor volutpat et neque.</li>
    <li><svg viewBox="0 0 15 13"><path d="M1 7 L5 11 L14 1" fill="none" stroke="#e50914" stroke-width="3"/></svg>Aliquam in sapien eget tellus molestie mattis.</li>
    <li><svg viewBox="0 0 15 13"><path d="M1 7 L5 11 L14 1" fill="none" stroke="#e50914" stroke-width="3"/></svg>Etiam ut massa dolor, at congue elit.</li>
    <li><svg viewBox="0 0 15 13"><path d="M1 7 L5 11 L14 1" fill="none" stroke="#e50914" stroke-width="3"/></svg>Nam ut sapien vitae erat consequat egestas.</li>
  </ul>

  <div class="video-player">
    <div class="video-frame" role="img" aria-label="Video still of a coach speaking in a garden setting"></div>
    <svg class="video-play" viewBox="0 0 66 50">
      <rect x="1" y="1" width="64" height="48" rx="12" fill="#e8e8e8" stroke="#bbb"/>
      <polygon points="25,14 25,36 44,25" fill="#555"/>
    </svg>
    <span class="video-brand">Cliphub</span>
    <div class="video-controls">
      <svg width="16" height="16" viewBox="0 0 16 16"><polygon points="3,2 3,14 14,8" fill="#222"/></svg>
      <div class="video-progress"></div>
      <span>0:00 / 0:00</span>
      <svg width="18" height="14" viewBox="0 0 18 14"><polygon points="1,5 5,5 9,1 9,13 5,9 1,9" fill="#333"/><path d="M12 4 Q14 7 12 10 M14 2 Q17 7 14 12" fill="none" stroke="#333"/></svg>
      <svg width="22" height="16" viewBox="0 0 22 16"><rect x="1" y="1" width="20" height="14" fill="#fff" stroke="#333"/><rect x="8" y="6" width="11" height="7" fill="#333"/></svg>
    </div>
  </div>

  <a class="feature-tile tile-how" href="#how-we-work">
    <div class="tile-photo" role="img" aria-label="Photo of a smiling business team"></div>
    <div class="tile-label">how we work?</div>
  </a>
  <a class="feature-tile tile-testimonials" href="#testimonials">
    <div class="tile-photo" role="img" aria-label="Photo of a confident client in a business suit"></div>
    <div class="tile-label">testimonials</div>
  </a>

  <form class="newsletter">
    <h2 class="newsletter-title">newsletter</h2>
    <p class="newsletter-text">Just fill in your email ID &amp; subscribe to our informative monthly newsletter</p>
    <input class="newsletter-input" type="email" aria-label="Email address">
    <button class="newsletter-submit" type="button">submit</button>
  </form>

  <footer class="site-footer">
    <span class="copyright">Copyright Brightmoor Pathways 2009</span>
    <a>Sitemap</a><span class="sep">|</span><a>Privacy Policy</a><span class="sep">|</span><a>Terms of Use</a>
  </footer>
</div>
</body>
</html>
```